K7 Digital Stationery Design Project

We are looking to have stationary designs created for our company branding materials. We are looking for the following to be created.
1. Business Cards (front & back)
2. Letterhead
3. Envelopes #10
We are a new web design, development and marketing firm. Primary color scheme is desired to be blue/grey/white. This web start-up is owned and operated by individuals with 15+ years experience each in the industry so should not look as though it is a start-up by young/inexperienced individuals.
We build website & custom applications/software. In addition we provide the full spectrum of web marketing solutions including SEO, PPC, Social Media, Branding, Content Marketing and PR.
Please let us know if you have any questions. Looking forward to seeing all the amazing design ideas.
Attached is our logo.
Thanks!
Target Market(s)
Company will be nearly 100% business to business sales. Looking to work with companies that are already established, with a website, who want to take their website and/or online marketing efforts to the next level.
Industry/Entity Type
Marketing
Look and feel

```html
<!DOCTYPE html>
<html lang="en">
<head>
<meta charset="utf-8">
<title>K7 Digital — Business Card</title>
<link rel="stylesheet" href="https://fonts.googleapis.com/css2?family=Jost:wght@400;500;600;700&display=swap">
<style>
  :root {
    --page-bg: #ffffff;
    --ink: #111111;
    --charcoal: #3d3d3f;
    --slate: #6d6e71;
    --mist: #e6e7e8;
    --silver: #bcbec0;
    --card-edge: #a7a9ac;
    --blue-deep: #1d75bc;
    --blue-mid: #1a87c8;
    --cyan: #00aedb;
    --white: #ffffff;
  }
  * { margin: 0; padding: 0; box-sizing: border-box; }
  html, body {
    width: 1200px; height: 1000px; overflow: hidden;
    background: var(--page-bg);
    font-family: "Jost", sans-serif;
  }
  .canvas { position: relative; width: 1200px; height: 1000px; }

  .label {
    position: absolute;
    font-weight: 500; font-size: 27px; color: var(--ink);
    line-height: 1;
  }
  .label--row { left: 122px; top: 438px; }
  .label--front { left: 525px; top: 168px; }
  .label--back { left: 898px; top: 168px; }

  .card {
    position: absolute;
    width: 302px; height: 512px;
    border-radius: 12px;
    overflow: hidden;
  }
  .card--front { left: 412px; top: 215px; background: var(--white); border: 1px solid var(--card-edge); }
  .card--back {
    left: 788px; top: 213px;
    background: linear-gradient(180deg, var(--cyan) 0%, var(--blue-mid) 60%, var(--blue-deep) 100%);
  }

  .card__art--front {
    position: absolute; left: 0; right: 0; top: 208px; bottom: 0;
    background: linear-gradient(165deg, var(--mist) 0%, var(--silver) 30%, var(--blue-mid) 60%, var(--slate) 100%);
  }
  .card__art--back {
    position: absolute; left: 0; right: 0; top: 0; height: 340px;
  }

  .brand { position: absolute; text-align: center; }
  .brand__name {
    display: flex; align-items: center; justify-content: center; gap: 7px;
    font-weight: 700; font-size: 22px; letter-spacing: 0.2px; line-height: 1;
  }
  .brand__dot { width: 12px; height: 12px; border-radius: 50%; display: inline-block; }
  .brand__tagline { font-weight: 500; font-size: 7.4px; margin-top: 4px; white-space: nowrap; }

  .card--front .brand { left: 0; right: 0; top: 150px; }
  .card--front .brand__name { color: var(--charcoal); }
  .card--front .brand__dot { background: var(--cyan); }
  .card--front .brand__tagline { color: var(--charcoal); }

  .card--back .brand { left: 25px; top: 230px; text-align: left; }
  .card--back .brand__name { color: var(--white); justify-content: flex-start; }
  .card--back .brand__dot { background: var(--white); }
  .card--back .brand__tagline { color: var(--white); }

  .contact { position: absolute; left: 26px; top: 358px; color: var(--white); }
  .contact__name { font-weight: 700; font-size: 28px; line-height: 1; }
  .contact__role { font-weight: 500; font-size: 14px; margin-top: 5px; }
  .contact__line { font-weight: 500; font-size: 14px; }
  .contact__email { margin-top: 14px; }
  .contact__phone { margin-top: 6px; }
</style>
</head>
<body>
<div class="canvas">
  <div class="label label--row">Business Card</div>
  <div class="label label--front">Front</div>
  <div class="label label--back">Back</div>

  <section class="card card--front">
    <div class="card__art--front" role="img" aria-label="Layered geometric shapes in grey and blue"></div>
    <div class="brand">
      <div class="brand__name"><span class="brand__dot"></span>K7 DIGITAL</div>
      <div class="brand__tagline">Web Design, Development and Marketing</div>
    </div>
  </section>

  <section class="card card--back">
    <div class="card__art--back" role="img" aria-label="Fine crossing line pattern over the blue background"></div>
    <div class="brand">
      <div class="brand__name"><span class="brand__dot"></span>K7 DIGITAL</div>
      <div class="brand__tagline">Web Design, Development and Marketing</div>
    </div>
    <div class="contact">
      <div class="contact__name">Name here</div>
      <div class="contact__role">CEO</div>
      <div class="contact__line contact__email">email@k7digital.com</div>
      <div class="contact__line contact__phone">5550-12345</div>
    </div>
  </section>
</div>
</body>
</html>
```